Business Card Design

Attached is my current Business card I do not like it but I must save the logo portion of it. Don't like the color or the lettering am looking for more architectural look in grays or taupe with the green more of a charturese color and the blue a charcoal color on a textured paper that looks more like something high-end that would appeal to an architect or a designer. We make concrete decorative items such as concrete fireplaces, sinks, tops and more.

Target Market(s)

Architects designers of Commercial and Residential - artistic features

Industry/Entity Type

Architect

Contact Information for Business Card

Marla T. Quinby President and Marketing Director
602-471-8836
email marla@quillstoneworks.example
Showroom "Valtique Design Center" 4128 W Larkmoor Scottsdale AZ
Fax: 602-713-4429

Font styles to use
Sans Serif

Requirements
Must have
• Architectural
Natural and earthy colors with a touch of color in the existing attached

```html
<!DOCTYPE html>
<html lang="en">
<head>
<meta charset="utf-8">
<title>Quillstone Works — Business Card</title>
<link href="https://fonts.googleapis.com/css2?family=Open+Sans:wght@400;600;700&display=swap" rel="stylesheet">
<style>
  :root {
    --stage: #000000;
    --stage-glow: #0d0d0d;
    --taupe: #b7ab99;
    --taupe-light: #cdc3b4;
    --chartreuse: #b5cc2e;
    --charcoal: #3b3b3d;
    --paper: #fbfaf7;
    --ink: #2e2d2b;
    --text: #1c1c1c;
  }
  * { margin: 0; padding: 0; box-sizing: border-box; }
  html, body { width: 1200px; height: 1000px; overflow: hidden; }
  body {
    position: relative;
    background: radial-gradient(ellipse at center, var(--stage-glow) 0%, var(--stage) 70%);
    font-family: "Open Sans", sans-serif;
    color: var(--text);
  }
  .card {
    position: absolute;
    left: 250px;
    width: 699px;
    background: var(--paper);
    overflow: hidden;
  }
  .card--front { top: 77px; height: 410px; }
  .card--back { top: 513px; height: 409px; }

  .front__panel {
    position: absolute; left: 0; top: 0; width: 100%; height: 217px;
    background: linear-gradient(160deg, var(--taupe-light) 0%, var(--taupe) 70%);
  }
  .accent-band { position: absolute; left: 0; width: 100%; height: 21px; background: var(--charcoal); }
  .card--front .accent-band { bottom: 0; }
  .card--back .accent-band { top: 0; }

  .brand {
    position: absolute;
    left: 0; width: 100%;
    display: flex;
    justify-content: center;
    align-items: center;
    gap: 16px;
  }
  .card--front .brand { top: 274px; }
  .card--back .brand { top: 185px; }
  .brand__square {
    width: 34px; height: 34px;
    background: var(--chartreuse);
    flex: none;
  }
  .brand__name {
    font-size: 46px;
    font-weight: 400;
    letter-spacing: -0.5px;
    color: var(--ink);
    line-height: 1;
  }

  .holder { position: absolute; left: 20px; top: 34px; }
  .holder__name { font-size: 17px; font-weight: 700; line-height: 1.2; color: var(--text); }
  .holder__title { font-size: 10px; line-height: 1.2; color: var(--text); }

  .contact-strip { position: absolute; left: 0; bottom: 0; width: 100%; height: 126px; background: var(--taupe); }
  .contact {
    position: absolute;
    top: 45px;
    font-size: 15px;
    line-height: 21.5px;
    color: var(--text);
  }
  .contact--address { left: 23px; }
  .contact--lines { left: 450px; }
</style>
</head>
<body>
  <section class="card card--front">
    <div class="front__panel" role="img" aria-label="Large faint brand emblem decoration in soft taupe tones"></div>
    <div class="brand">
      <span class="brand__square"></span>
      <span class="brand__name">Quillstone Works</span>
    </div>
    <div class="accent-band"></div>
  </section>

  <section class="card card--back">
    <div class="accent-band"></div>
    <div class="holder">
      <div class="holder__name">Marla T.</div>
      <div class="holder__title">Quinby President and Marketing Director</div>
    </div>
    <div class="brand">
      <span class="brand__square"></span>
      <span class="brand__name">Quillstone Works</span>
    </div>
    <div class="contact-strip">
      <div class="contact contact--address">
        Address:<br>
        Showroom "Valtique Design Center" 4128<br>
        W Larkmoor Scottsdale AZ
      </div>
      <div class="contact contact--lines">
        Phone: 602-471-8836<br>
        Fax: 602-713-4429<br>
        marla@quillstoneworks.example
      </div>
    </div>
  </section>
</body>
</html>
```